Lone Star Wetland Flora Stewardship Guild

We need to design the home page of this new website. We would like a fun website design for provides as a resource for members and information for potential members.
Please design so that we can see a portion of background on each side on the website.
I just need the final design files psd no coding needed.
Attached is their logo (colors are not 100% set in stone either so can mess with those as I did in the quick mockup attached)
Attached is a pdf newsletter they send out, you can get a feel for them and what they are about. The design is crappy and we are here to fix that going forward and we are starting with the website.
Here are some quick example websites (design style is open)
- I attached a quick mockup i did just for a content visual but by all means do what you want.
- http://www.brindlecourtleaders.org/
- http://www.qvelto.org/
- http://preview.plimworks7.com/view.php?cat=layoutpacks&host=gridcrafthub&temp=venrolite
- http://www.ploughvale.org/
- http://www.townmarrow.org/
- http://www.projectkindlecoat.org/
here are some of the other chapters website (pretty bad!)
and here are some of the others:
- http://www.zrelkq.org/
- http://ovtu.org/
- http://www.lirvx.org/
Content Items that need to be included:
1. Logo
2. Menu - home, about, members, resources, events, membership, contact
3. Become a member - button or action
4. social links - friendwall, jobrungo, clipzora
5. banner - that needs to explain their purpose "Promoting environmental stewardship through operations, research, education and outreach" (or this can be worked into the design)
6. Upcoming event (s)
7. Advertisement - members can place an ad on the website, this can be a placeholder for now
8. newsletter signup
9. advertise with us - this link can be in the footer
30-60 years of age, succesfull (household budgets of 120K+ men and women that live in texas.
Education

```html
<!DOCTYPE html>
<html lang="en">
<head>
<meta charset="utf-8">
<title>Lone Star Wetland Flora Stewardship Guild</title>
<link href="https://fonts.googleapis.com/css2?family=Open+Sans:wght@400;600&family=Oswald:wght@400&display=swap" rel="stylesheet">
<style>
:root{
  --navy:#0d3f8a;
  --rose:#e04a5c;
  --rose-dark:#c93c4e;
  --gold:#f3b640;
  --gold-light:#f7c452;
  --ink:#4a4a4a;
  --muted:#9a9a9a;
  --line:#e6e6e6;
  --footer:#0b0b0b;
}
*{box-sizing:border-box;margin:0;padding:0}
html,body{width:1030px;height:1200px;overflow:hidden;background:#fff;font-family:"Open Sans",sans-serif;color:var(--ink)}
.page{position:relative;width:1030px;height:1200px}
.backdrop{position:absolute;left:0;top:0;width:1030px;height:550px;
  background:linear-gradient(180deg,#8fbde8 0%,#c9def2 28%,#6f9a52 40%,#5c7d4a 48%,#8aa9c2 60%,#9db08a 80%,#6f7f5e 100%)}
.abs{position:absolute}
.brand{left:148px;top:30px;width:200px;height:90px}
.brand-mark{position:absolute;left:0;top:8px;width:36px;height:36px;border-radius:50%;background:var(--rose)}
.brand-name{position:absolute;left:46px;top:6px;font-size:34px;font-weight:600;color:var(--navy);letter-spacing:1px}
.brand-full{position:absolute;left:0;top:56px;font-size:8.5px;font-weight:600;color:#222;width:240px}
.btn{display:inline-block;border-radius:4px;color:#fff;text-align:center}
.join{left:750px;top:53px;width:133px;height:34px;line-height:34px;background:var(--navy);font-size:13px}
.nav{left:148px;top:144px;width:735px;height:46px;background:var(--rose);border-radius:4px 4px 0 0;display:flex;padding-left:28px}
.nav a{color:#fff;text-decoration:none;font-size:14px;line-height:46px;margin-right:41px}
.hero{left:148px;top:190px;width:735px;height:360px;
  background:linear-gradient(180deg,#9cc0e6 0%,#dbe7f0 22%,#7fa54a 30%,#9cc04a 40%,#3d6fa8 52%,#3a679a 66%,#6f9a3a 78%,#4f7430 100%)}
.caption{left:148px;top:490px;width:735px;height:60px;background:rgba(40,40,40,.72);color:#fff;font-family:"Oswald",sans-serif;font-size:19px;line-height:60px;text-align:center;letter-spacing:-.2px}
.caption svg{position:absolute;top:24px}
.welcome h1{font-size:19px;font-weight:400;color:#333}
.welcome h1 span{color:var(--navy);font-weight:600}
.welcome{left:148px;top:571px;width:510px}
.welcome p{margin-top:6px;font-size:9.2px;line-height:17.6px;color:var(--muted)}
.read{margin-top:10px;width:82px;height:29px;line-height:29px;background:var(--navy);font-size:11px}
.events-title{left:148px;top:764px;width:510px;font-size:16px;color:#555;padding-bottom:12px;border-bottom:1px solid var(--line)}
.event{left:148px;width:510px;height:112px}
.event .thumb{position:absolute;left:0;top:0;width:144px;height:112px}
.event .body{position:absolute;left:163px;top:0;width:335px}
.event h3{font-size:13px;font-weight:400;color:#777}
.event p{margin-top:8px;font-size:9.2px;line-height:17.6px;color:#aaa}
.event .more{display:block;margin-top:6px;font-size:10.5px;color:#666}
.newsletter{left:670px;top:576px;width:213px;height:166px;background:var(--gold-light)}
.newsletter h2{height:33px;line-height:33px;background:var(--gold);color:#fff;font-size:16.5px;font-weight:400;text-align:center}
.newsletter p{margin-top:6px;font-size:9px;line-height:16px;color:#fff;text-align:center}
.field{position:absolute;background:#fff;border-radius:3px;font-size:8.5px;color:#777;padding-left:11px;line-height:31px;height:31px}
.signup{position:absolute;left:134px;top:120px;width:67px;height:30px;line-height:30px;background:var(--rose);font-size:13.5px}
.ad{left:669px;top:768px;width:214px;height:295px}
.ad .art{position:absolute;left:0;top:0;width:214px;height:217px;background:linear-gradient(180deg,#2f7fb5,#1c4f7f 60%,#222)}
.ad .sponsor{position:absolute;left:0;top:217px;width:214px;height:78px;background:#e2e2e2;text-align:center;font-size:19px;font-weight:600;color:#222;line-height:78px}
.footer{left:0;top:1096px;width:1030px;height:104px;background:var(--footer)}
.f-brand{left:148px;top:18px;font-size:24px;font-weight:600;color:#9a9a9a}
.f-brand small{display:block;font-size:7px;font-weight:400;color:#555;margin-top:4px}
.copy{left:303px;top:27px;font-size:10.5px;color:#aaa}
.f-links{left:303px;top:57px;font-size:9.5px;color:#aaa;word-spacing:2px}
.advertise{left:759px;top:18px;width:124px;height:29px;line-height:29px;background:var(--rose);font-size:12px;font-weight:600}
.social{left:800px;top:62px;display:flex;gap:6px}
.social span{display:block;width:23px;height:23px;border:1px solid #666;border-radius:50%}
</style>
</head>
<body>
<div class="page">
  <div class="backdrop" role="img" aria-label="Lake with floating lily pads and trees under a blue sky"></div>

  <div class="abs brand">
    <span class="brand-mark"></span>
    <span class="brand-name">LSWFSG</span>
    <span class="brand-full">Lone Star Wetland Flora Stewardship Guild</span>
  </div>
  <a class="abs btn join">Become a member</a>

  <nav class="abs nav">
    <a>Home</a><a>About Us</a><a>Members</a><a>Resources</a><a>Events</a><a>Membership</a><a>Contact Us</a>
  </nav>

  <div class="abs hero" role="img" aria-label="Wide wetland with marsh grass and calm blue water"></div>
  <div class="abs caption">
    <svg style="left:26px" width="10" height="14" viewBox="0 0 10 14"><path d="M8 1 2 7l6 6" fill="none" stroke="#fff" stroke-width="2"/></svg>
    Promoting Environmental Stewardship Through Operations, Research, Education
    <svg style="right:22px" width="10" height="14" viewBox="0 0 10 14"><path d="M2 1l6 6-6 6" fill="none" stroke="#fff" stroke-width="2"/></svg>
  </div>

  <section class="abs welcome">
    <h1>Welcome To <span>Wetland Flora Stewardship</span></h1>
    <p>Lorem ipsum dolor sit amet, consectetur adipisc ng elit. Proin ultricies vestibulum velit, bibendum condimentum metus faucibus sed. Lorem ipsum dolor sit amet, consectetur adipisc ng elit. Proin ultricies vestibulum velit, bibendum condimentum metus faucibus sed. Lorem ipsum dolor sit amet, consectetur adipisc ng elit. Proin ultricies vestibulum velit, bibendum condimentum metus faucibus sed. Lorem ipsum dolor sit amet, consectetur adipisc ng elit. Proin ultricies vestibulum velit, bibendum condimentum metus faucibus sed. Lorem ipsum dolor sit amet, consectetur adipisc ng elit. Proin ultricies vestibulum</p>
    <a class="btn read">Read More</a>
  </section>

  <h2 class="abs events-title" style="font-weight:400">Upcoming Event</h2>

  <article class="abs event" style="top:818px">
    <div class="thumb" role="img" aria-label="Pond edged with reeds and trees" style="background:linear-gradient(180deg,#dfe9ef,#6f9a4a 40%,#5d7d52 70%,#8aa08a)"></div>
    <div class="body">
      <h3>Lorem ipsum dolor sit amet</h3>
      <p>Lorem ipsum dolor sit amet, conse ctetur adipisicing elit, sed do eius mod tempor incididunt ut labore et dolore magna aliqua. Quisque bibendum eros quis elit Lorem ipsum dolor sit amet, conse ctetur adipisicing elit, sed do eius mod tempor incididunt ut labore et dolore magna aliqua.</p>
      <a class="more">Read More +</a>
    </div>
  </article>

  <article class="abs event" style="top:950px">
    <div class="thumb" role="img" aria-label="Water lily pads among tall reeds" style="background:linear-gradient(180deg,#7fa08a,#3f6a5a 50%,#5a8a4a)"></div>
    <div class="body">
      <h3>Lorem ipsum dolor sit amet</h3>
      <p>Lorem ipsum dolor sit amet, conse ctetur adipisicing elit, sed do eius mod tempor incididunt ut labore et dolore magna aliqua. Quisque bibendum eros quis elit Lorem ipsum dolor sit amet, conse ctetur adipisicing elit, sed do eius mod tempor incididunt ut labore et dolore magna aliqua.</p>
      <a class="more">Read More +</a>
    </div>
  </article>

  <aside class="abs newsletter">
    <h2>Newsletter Signup</h2>
    <p>Pellentesque habitant morbi tristique<br>senectus et netus et malesuada fames</p>
    <div class="field" style="left:13px;top:78px;width:188px">Name</div>
    <div class="field" style="left:13px;top:120px;width:110px">Email</div>
    <a class="btn signup">Sign Up</a>
  </aside>

  <aside class="abs ad">
    <div class="art" role="img" aria-label="Advertisement product packaging for AquaBright PRO water treatment"></div>
    <div class="sponsor">PondWise Labs</div>
  </aside>

  <footer class="abs footer">
    <div class="abs f-brand">LSWFSG<small>Lone Star Wetland Flora Stewardship Guild</small></div>
    <div class="abs copy">©2014 Wetland Flora Stewardship , All Rights Reserved.</div>
    <div class="abs f-links">Home &nbsp;| &nbsp;About &nbsp;| &nbsp;Members &nbsp;&nbsp;| &nbsp;resources &nbsp;| &nbsp;Contact</div>
    <a class="abs btn advertise">Advertise with us</a>
    <div class="abs social" aria-label="friendwall, jobrungo, clipzora"><span></span><span></span><span></span></div>
  </footer>
</div>
</body>
</html>
```